Disease outbreak warning

I need a flyer that explains to hunters how to act as frontline responders to potential disease outbreaks in wildlife populations. In this case the disease is African Swine Fever. We need an at a glance style with plenty of colour and that’s very easy to read.

I HAVE ATTACHED SOME EXISTING FLYERS FROM OVERSEAS ETC THAT CONTAIN SOME OF THE RELEVANT INFO. THEY ARE TO BE USED AS A GUIDE ONLY.
Updates

Need to see some more options. We have some that can be developed successfully but we’d like to see some more options that will suit a national campaign.

Target Market(s)

Australian hunters encountering wild pigs. Typical age is from 18 to 32 but can be older. Male or female.

Colors

Designer to choose colors to be used in the design.

Requirements
Must have
• The KWOTL logo (supplied). It should be relatively small at the bottom of the page. Plus we need room for two or three other logos that can be overprinted on the project if required.
• Must have information for hunters as the main focus.
Nice to have
• A double sided flyer.
Should not have
• US spelling.

```html
<!DOCTYPE html>
<html lang="en-AU">
<head>
<meta charset="utf-8">
<title>African Swine Fever – Hunter Flyer</title>
<link rel="stylesheet" href="https://fonts.googleapis.com/css2?family=Open+Sans:ital,wdth,wght@0,75..100,400..800;1,75..100,400..800&display=swap">
<style>
  :root{
    --stage:#2e3331;
    --paper:#e6e4de;
    --ink:#111111;
    --green:#0c7a5c;
    --green-dark:#0a4f38;
    --green-deep:#073a29;
    --cream:#fbf6e6;
    --white:#ffffff;
    --muted:#d8d8d2;
  }
  *{box-sizing:border-box;margin:0;padding:0}
  html,body{width:1200px;height:857px;overflow:hidden;background:var(--stage)}
  body{font-family:"Open Sans",Arial,sans-serif;position:relative}

  .page{position:absolute;top:28px;width:566px;height:800px;overflow:hidden}
  .page--back{left:34px;background:var(--paper)}
  .page--front{left:600px;background:var(--cream)}

  .back-corner{position:absolute;left:0;top:0}
  .brand{position:absolute;left:22px;top:28px;display:flex;align-items:center;gap:8px}
  .brand__dot{width:46px;height:46px;border-radius:50%;background:var(--white)}
  .brand__name{color:var(--white);font-weight:800;font-size:20px;letter-spacing:1px}

  .headline{position:absolute;right:30px;text-align:right}
  .headline__main{font-weight:800;color:var(--ink);line-height:.95;font-stretch:87.5%}
  .headline__sub{color:var(--green);font-weight:800;font-style:italic;font-stretch:75%;margin-top:6px}

  .page--back .headline{top:80px}
  .page--back .headline__main{font-size:58px;text-transform:uppercase}
  .page--back .headline__main span{display:block;font-size:40px}
  .page--back .headline__sub{font-size:23px}

  .steps-lines{position:absolute;left:0;top:0}
  .pig-badge{position:absolute;left:52px;top:372px;width:136px;height:136px;border-radius:50%;
    background:radial-gradient(circle,#f1ece6 0 55%,#d9cfc8 100%);border:4px solid #c9c4bd}
  .pig-badge__art{position:absolute;left:22px;top:38px;width:84px;height:52px;border-radius:40% 45% 30% 30%;background:#1a1a1a}

  .step{position:absolute;height:62px;display:flex;align-items:center;
    background:linear-gradient(90deg,var(--green) 0%,var(--green-dark) 100%);
    clip-path:polygon(0 0,86% 0,100% 50%,86% 100%,0 100%);
    box-shadow:0 3px 6px rgba(0,0,0,.3)}
  .step__icon{width:62px;height:62px;background:var(--green-deep);display:flex;align-items:center;justify-content:center;flex:none}
  .step__icon svg{width:30px;height:30px}
  .step__text{color:var(--white);font-weight:700;font-style:italic;font-stretch:75%;font-size:15px;line-height:1.05;padding:0 50px 0 14px}

  .back-footer{position:absolute;left:0;bottom:0;width:566px;height:110px;background:var(--ink);
    clip-path:polygon(0 0,100% 30%,100% 100%,0 100%)}
  .back-footer__call{position:absolute;left:26px;top:30px;color:var(--muted);font-weight:700;font-size:19px;font-stretch:87.5%}
  .back-footer__web{position:absolute;right:30px;bottom:16px;color:var(--muted);font-weight:700;font-size:19px;font-stretch:87.5%}

  .front-photo{position:absolute;inset:0;
    background:
      radial-gradient(ellipse 75% 45% at 80% 15%,rgba(251,246,230,1) 0%,rgba(251,246,230,.9) 40%,rgba(251,246,230,0) 75%),
      linear-gradient(180deg,#c8b26a 0%,#b9a35a 35%,#8d8a45 55%,#5f6a2c 75%,#3f4d1e 100%)}
  .front-photo__subject{position:absolute;left:120px;top:420px;width:300px;height:200px;border-radius:45%;
    background:radial-gradient(ellipse,rgba(58,38,26,.75) 0%,rgba(58,38,26,0) 70%)}

  .page--front .headline{top:150px;right:28px}
  .page--front .headline__main{font-size:76px;font-stretch:100%}
  .page--front .headline__main span{display:block;font-size:50px;font-weight:700}
  .page--front .headline__sub{font-size:27px}
  .headline__lede{margin-top:10px;font-size:16px;line-height:1.3;color:var(--ink);font-stretch:87.5%}

  .front-stripe{position:absolute;left:0;top:0}
  .front-seal{position:absolute;left:48px;top:590px;width:168px;height:168px;border-radius:50%;
    background:var(--white);border:8px solid var(--green);display:flex;align-items:center;justify-content:center}
  .front-seal__name{color:var(--green-dark);font-weight:800;font-size:30px;letter-spacing:1px}
</style>
</head>
<body>

<section class="page page--back">
  <svg class="back-corner" width="566" height="300" viewBox="0 0 566 300">
    <polygon points="0,0 230,0 0,250" fill="var(--ink)"/>
    <polygon points="240,0 272,0 0,296 0,262" fill="var(--green)"/>
    <polygon points="282,0 292,0 0,318 0,307" fill="var(--green)"/>
  </svg>
  <div class="brand"><span class="brand__dot"></span><span class="brand__name">KWOTL</span></div>

  <header class="headline">
    <h1 class="headline__main">African<span>Swine Fever</span></h1>
    <p class="headline__sub">Don't spreade this deadly disease</p>
  </header>

  <svg class="steps-lines" width="566" height="800" viewBox="0 0 566 800" fill="none" stroke="#6f7d78" stroke-width="2">
    <path d="M120 360 A80 80 0 0 1 200 440" stroke="#b7bdb9" stroke-width="8"/>
    <path d="M200 440 A80 80 0 0 1 120 520" stroke="#b7bdb9" stroke-width="8"/>
    <path d="M120 520 A80 80 0 0 1 40 440" stroke="#b7bdb9" stroke-width="8"/>
    <path d="M160 370 L205 330 L225 330"/>
    <path d="M195 410 L215 390 L240 390"/>
    <path d="M200 455 L230 470 L250 470"/>
    <path d="M175 500 L195 540 L215 540"/>
    <path d="M110 525 L110 590 L140 600"/>
    <g fill="var(--green)" stroke="none">
      <circle cx="160" cy="370" r="5"/><circle cx="195" cy="410" r="5"/>
      <circle cx="200" cy="455" r="5"/><circle cx="175" cy="500" r="5"/>
      <circle cx="110" cy="525" r="5"/>
    </g>
  </svg>

  <div class="pig-badge" role="img" aria-label="Black silhouette of a domestic pig">
    <div class="pig-badge__art"></div>
  </div>

  <div class="step" style="left:225px;top:300px;width:300px">
    <div class="step__icon"><svg viewBox="0 0 30 30"><rect x="5" y="8" width="8" height="16" fill="#fff"/><rect x="16" y="6" width="9" height="18" fill="#fff"/></svg></div>
    <p class="step__text">Clean &amp; disinfect your equipment on site</p>
  </div>
  <div class="step" style="left:240px;top:380px;width:300px">
    <div class="step__icon"><svg viewBox="0 0 30 30"><polygon points="4,14 15,5 26,14" fill="#fff"/><rect x="7" y="14" width="16" height="11" fill="#fff"/></svg></div>
    <p class="step__text">Do not visit farms unless it is necessary</p>
  </div>
  <div class="step" style="left:250px;top:460px;width:300px">
    <div class="step__icon"><svg viewBox="0 0 30 30"><circle cx="15" cy="6" r="3.5" fill="#fff"/><rect x="12" y="11" width="6" height="15" fill="#fff"/></svg></div>
    <p class="step__text">Do not carry pigs or pork products</p>
  </div>
  <div class="step" style="left:215px;top:540px;width:300px">
    <div class="step__icon"><svg viewBox="0 0 30 30"><rect x="12" y="4" width="6" height="16" rx="3" fill="#fff"/><circle cx="15" cy="22" r="5" fill="#fff"/></svg></div>
    <p class="step__text">Report soon for sick pigs</p>
  </div>
  <div class="step" style="left:140px;top:620px;width:300px">
    <div class="step__icon"><svg viewBox="0 0 30 30"><ellipse cx="15" cy="16" rx="11" ry="7" fill="#fff"/></svg></div>
    <p class="step__text">Clean &amp; disinfect your hunting trophies before living the area</p>
  </div>

  <footer class="back-footer">
    <p class="back-footer__call">Call us : 123-456-7890</p>
    <p class="back-footer__web">Website : kwotlfield.org</p>
  </footer>
</section>

<section class="page page--front">
  <div class="front-photo" role="img" aria-label="Photograph of a wild boar running through long grass in warm morning light">
    <div class="front-photo__subject"></div>
  </div>

  <header class="headline">
    <h2 class="headline__main">African<span>swine fever</span></h2>
    <p class="headline__sub">Don't spreade this deadly disease</p>
    <p class="headline__lede">Lorem ipsum dolor sit amet, consectetur<br>adipiscing elit, sed do eiusmod tempor incididunt<br>ut labore et dolore magna aliqua.</p>
  </header>

  <svg class="front-stripe" width="566" height="800" viewBox="0 0 566 800">
    <polygon points="0,470 0,800 200,800" fill="var(--ink)"/>
    <polygon points="0,440 0,470 200,800 232,800" fill="var(--green)"/>
  </svg>
  <div class="front-seal"><span class="front-seal__name">KWOTL</span></div>
</section>

</body>
</html>
```